Flyer for the Lumen 2025 Conference

I am looking to produce a flyer for our upcoming conference, Lumen 2025. This is an annual conference that we plan to publicize on social media. The ideal designer will create a flyer that is eye-catching and effectively communicates the key information. Please see attached our logo, speaker photo, and flyer content.

Target Market(s)

All demographics

Industry/Entity Type

Christian

Font styles to use
Sans Serif

Requirements
Should not have
• Cross, church

```html
<!DOCTYPE html>
<html lang="en">
<head>
<meta charset="utf-8">
<title>Lumen 2025 Prophetic Conference Flyer</title>
<link rel="stylesheet" href="https://fonts.googleapis.com/css2?family=Oswald:wght@400;500;600;700&family=Montserrat:ital,wght@0,400;0,500;0,600;0,700;1,400&display=swap">
<style>
  :root {
    --orange: #f7941d;
    --blue-deep: #0d2f52;
    --blue-mid: #1a5f95;
    --blue-light: #3f8fc4;
    --band-blue: #0b5891;
    --navy: #0b2240;
    --white: #ffffff;
  }
  html, body {
    margin: 0;
    padding: 0;
    width: 802px;
    height: 1200px;
    overflow: hidden;
    background: var(--orange);
  }
  .flyer {
    position: relative;
    width: 802px;
    height: 1200px;
    overflow: hidden;
  }
  .flyer__art {
    position: absolute;
    inset: 0;
    display: block;
  }
  .headline { font-family: "Oswald", sans-serif; }
  .body-text { font-family: "Montserrat", sans-serif; }
</style>
</head>
<body>
<main class="flyer">
  <svg class="flyer__art" width="802" height="1200" viewBox="0 0 802 1200" xmlns="http://www.w3.org/2000/svg">
    <defs>
      <radialGradient id="smoke-glow" cx="0.45" cy="0.18" r="0.85">
        <stop offset="0" stop-color="var(--blue-light)"/>
        <stop offset="0.45" stop-color="var(--blue-mid)"/>
        <stop offset="1" stop-color="var(--blue-deep)"/>
      </radialGradient>
      <linearGradient id="speaker-tone" x1="0" y1="0" x2="0" y2="1">
        <stop offset="0" stop-color="#2c5f93"/>
        <stop offset="0.35" stop-color="#1f6fc0"/>
        <stop offset="1" stop-color="#14508f"/>
      </linearGradient>
    </defs>

    <!-- Background panels -->
    <polygon class="panel panel--smoke" points="322,0 802,0 802,649 531,1200 0,1200 0,1010" fill="url(#smoke-glow)"/>

    <!-- Speaker photo area -->
    <path class="speaker-photo" role="img" aria-label="Portrait photo of the speaker in a blue suit and grey turtleneck"
          d="M88,90 Q95,40 160,42 Q230,44 236,100 L240,210 Q300,230 330,300 L370,560 L370,780 L0,780 L0,330 Q40,250 98,230 Z"
          fill="url(#speaker-tone)"/>

    <!-- Date band -->
    <polygon class="band band--dates" points="0,772 737,772 627,993 0,993" fill="var(--band-blue)"/>
    <!-- Info footer -->
    <polygon class="band band--info" points="0,993 627,993 531,1200 0,1200" fill="var(--navy)"/>

    <!-- Brand name -->
    <g class="brand">
      <circle cx="377" cy="102" r="10" fill="var(--orange)"/>
      <text class="body-text" x="525" y="127" text-anchor="middle" font-size="62" font-weight="400" fill="var(--white)" letter-spacing="2">SOLVANE</text>
    </g>

    <!-- Title -->
    <g class="title headline" text-anchor="middle">
      <text x="522" y="274" font-size="56" font-weight="500" fill="var(--white)" textLength="268" lengthAdjust="spacingAndGlyphs">LUMEN 2025 A</text>
      <text x="510" y="414" font-size="148" font-weight="700" fill="var(--orange)" textLength="468" lengthAdjust="spacingAndGlyphs">PROPHETIC</text>
      <text x="511" y="481" font-size="66" font-weight="500" fill="var(--white)" textLength="372" lengthAdjust="spacingAndGlyphs">CONFERENCE</text>
    </g>

    <!-- Topic and speaker -->
    <g class="topic" text-anchor="middle" fill="var(--white)">
      <text class="headline" x="512" y="579" font-size="36" font-weight="500" letter-spacing="4">TOPIC:</text>
      <text class="body-text" x="502" y="626" font-size="28" font-weight="700" textLength="504" lengthAdjust="spacingAndGlyphs">The Voice Of The LordSpeaker:</text>
      <text class="body-text" x="505" y="662" font-size="29" font-style="italic" font-weight="400" letter-spacing="1">Prophet Marcus Adeyemi</text>
    </g>

    <!-- Dates -->
    <g class="dates headline" text-anchor="middle">
      <g class="date">
        <text x="120" y="846" font-size="30" font-weight="500" fill="var(--white)">DECEMBER</text>
        <text x="120" y="910" font-size="68" font-weight="600" fill="var(--orange)">26TH</text>
        <text x="120" y="935" font-size="13" font-weight="500" fill="var(--white)">6:30PM - 9:00PM</text>
        <text x="120" y="952" font-size="13" font-weight="500" fill="var(--white)">SATURDAY</text>
      </g>
      <line x1="230" y1="795" x2="230" y2="971" stroke="var(--white)" stroke-width="2"/>
      <g class="date">
        <text x="327" y="846" font-size="30" font-weight="500" fill="var(--white)">DECEMBER</text>
        <text x="327" y="910" font-size="68" font-weight="600" fill="var(--orange)">27TH</text>
        <text x="327" y="935" font-size="13" font-weight="500" fill="var(--white)">6:30PM - 9:00PM</text>
        <text x="327" y="952" font-size="13" font-weight="500" fill="var(--white)">SATURDAY</text>
      </g>
      <line x1="435" y1="795" x2="435" y2="971" stroke="var(--white)" stroke-width="2"/>
      <g class="date">
        <text x="536" y="846" font-size="30" font-weight="500" fill="var(--white)">DECEMBER</text>
        <text x="536" y="910" font-size="68" font-weight="600" fill="var(--orange)">29TH</text>
        <text x="536" y="935" font-size="13" font-weight="500" fill="var(--white)">6:30PM - 9:00PM</text>
        <text x="536" y="952" font-size="13" font-weight="500" fill="var(--white)">SATURDAY</text>
      </g>
    </g>

    <!-- Location -->
    <g class="location body-text" fill="var(--white)">
      <text x="58" y="1066" font-size="19" font-weight="700">Location:</text>
      <text x="58" y="1089" font-size="15.5">The Harborview Performing Arts Center 218 Millbrook</text>
      <text x="58" y="1106" font-size="15.5">Street Eastfield, Maine 04110</text>
      <g class="icon icon--pin" transform="translate(40,1096)">
        <path d="M0,-12 a6,6 0 0 1 6,6 c0,5 -6,11 -6,11 c0,0 -6,-6 -6,-11 a6,6 0 0 1 6,-6 z" fill="none" stroke="var(--orange)" stroke-width="2.2"/>
        <circle cx="0" cy="-6" r="2" fill="var(--orange)"/>
        <line x1="-7" y1="6" x2="7" y2="6" stroke="var(--orange)" stroke-width="2"/>
      </g>
    </g>

    <!-- App banner -->
    <g class="app-banner">
      <path d="M0,1127 H511 a12,12 0 0 1 0,24 H0 Z" fill="var(--orange)"/>
      <text class="body-text" x="36" y="1145" font-size="15.5" font-weight="600" fill="var(--navy)">Download the Solvane App to stay updated on the event</text>
    </g>

    <!-- Contacts -->
    <g class="contacts body-text" fill="var(--white)" font-size="15" font-weight="500">
      <g class="icon icon--phone" transform="translate(40,1180)">
        <path d="M-6,-6 q2,-2 4,0 l2,3 q1,2 -1,3 q1,3 4,4 q1,-2 3,-1 l3,2 q2,2 0,4 q-3,3 -8,0 q-5,-3 -8,-8 q-3,-5 1,-7 z" fill="var(--white)"/>
      </g>
      <text x="58" y="1185">207 555 0142</text>
      <g class="icon icon--mail" transform="translate(194,1180)">
        <rect x="-8" y="-6" width="16" height="11" fill="none" stroke="var(--white)" stroke-width="1.6"/>
        <polyline points="-8,-6 0,1 8,-6" fill="none" stroke="var(--white)" stroke-width="1.6"/>
      </g>
      <text x="212" y="1185">contact@solvane.org</text>
      <g class="icon icon--globe" transform="translate(394,1180)" fill="none" stroke="var(--white)" stroke-width="1.5">
        <circle r="8"/>
        <ellipse rx="3.5" ry="8"/>
        <line x1="-8" y1="0" x2="8" y2="0"/>
      </g>
      <text x="410" y="1185">www.solvane.org</text>
    </g>
  </svg>
</main>
</body>
</html>
```